VineGlow Artbook for Okanagan Region, British Columbia

Creating an art book: VineGlow, for the Okanagan Wine Region in British Columbia, Canada. Would like smart, modern, clean and linear...cool, sexy urban, not ugly boring suburban... I need a cover that appeals to the wino in all of us! Title: VineGlow -Marla Pettivan
Updates
Thank you all kindly for your efforts. I have added some files so that you can get a sense of my aesthetic...it's never easy trying to figure it out, is it? I will hopefully have dimensions of book soon...cheers, Marla
would anyone please design a giant wine bottle with the wine label that looks like a label but says vineglow...just curious to see if it works as a design or not...thank you.
Target Market(s)
Designing this wine art book of quotes to wineries in Okanagan BC. Buyer is wine lover and tourist ready to spend his vacation bucks on this wonderful book!
Look and feel

```html
<!DOCTYPE html>
<html lang="en">
<head>
<meta charset="utf-8">
<title>VineGlow – Cover Options</title>
<link rel="stylesheet" href="https://fonts.googleapis.com/css2?family=Arimo:wght@400;700&display=swap">
<style>
  :root {
    --page-bg: #f4f4f4;
    --cover-bg: #f4f4f4;
    --cover-edge: #4a4a4a;
    --title-red: #c4101f;
    --ink: #111111;
  }
  html, body {
    margin: 0;
    padding: 0;
    overflow: hidden;
  }
  body {
    width: 1200px;
    height: 749px;
    background: var(--page-bg);
    position: relative;
    font-family: "Arimo", Arial, sans-serif;
  }
  .cover {
    position: absolute;
    top: 35px;
    width: 488px;
    height: 690px;
    background: var(--cover-bg);
    border: 1px solid var(--cover-edge);
    box-sizing: border-box;
  }
  .cover--top-author { left: 48px; }
  .cover--bottom-author { left: 650px; }

  .cover__title {
    position: absolute;
    margin: 0;
    font-family: "Arimo", Arial, sans-serif;
    font-weight: 700;
    font-size: 91px;
    line-height: 1;
    letter-spacing: 0;
    color: var(--title-red);
    white-space: nowrap;
  }
  .cover__author {
    position: absolute;
    margin: 0;
    font-family: "Arimo", Arial, sans-serif;
    font-weight: 400;
    font-size: 21px;
    line-height: 1;
    color: var(--ink);
    white-space: nowrap;
    text-align: right;
  }

  .cover--top-author .cover__author { right: 43px; top: 39px; }
  .cover--top-author .cover__title { left: 36px; top: 582px; }

  .cover--bottom-author .cover__title { left: 36px; top: 535px; }
  .cover--bottom-author .cover__author { right: 43px; top: 634px; }
</style>
</head>
<body>
  <section class="cover cover--top-author">
    <p class="cover__author">Marla Pettivan</p>
    <h1 class="cover__title">VineGlow</h1>
  </section>

  <section class="cover cover--bottom-author">
    <h1 class="cover__title">VineGlow</h1>
    <p class="cover__author">Marla Pettivan</p>
  </section>
</body>
</html>
```